MCP phase 1 web design

Meridale Capital Partners Ltd (MCP) is a challenger business to the traditional leasing market. We look for solutions to complex problems involving the funding of capital equipment within an office environment and then build documentation around the solution. We recently created a brief for a logo and successfully completed that assignment. We now need to create our first web site which is simply intended to be informative. To help interested designers we have attached a detailed brief that is broken into three sections. The first explains how we see the site developing over time from something quite straightforward initially to a full transaction capability. Whoever wins this competition will be expected to work with us into the future to help develop the site. Section 2 gives you a view about our likes and dislikes by reviewing some existing sites. Section 3 gives you the structure and content of the site based upon our likes and dislikes. We are by no means committed to the structure and if you believe it can be presented in a better way then please use your design. The text is fixed as content. The images to appear can be anything from photographs to line drawings again entirely at the designers whim. Currently we have a home page plus 5 subsidiary pages. A few things to help you:
1. The logo is fixed and should be amongst the downloads.
2. The colours we have are corporate and should be used.
3. The typeface we use within the business is "Verdana"
Good luck.

Industry/Entity Type

Business

```html
<!DOCTYPE html>
<html lang="en">
<head>
<meta charset="utf-8">
<title>Meridale Capital Partners Ltd</title>
<link href="https://fonts.googleapis.com/css2?family=Open+Sans:ital,wght@0,300;0,400;0,600;0,700;1,700&display=swap" rel="stylesheet">
<style>
:root{
  --blue:#1f6fc0;
  --blue-btn:#1b73c9;
  --blue-deep:#145fae;
  --blue-light:#3a8ee0;
  --ink:#333;
  --muted:#666;
  --grey-bar:#555;
  --line:#ddd;
  --panel:#f4f5f7;
}
*{box-sizing:border-box;margin:0;padding:0}
html,body{width:868px;height:1200px;overflow:hidden;background:#fff}
body{position:relative;font-family:"Open Sans",sans-serif;color:var(--ink);font-size:10px}
.abs{position:absolute}

/* header */
.header{left:0;top:0;width:868px;height:68px;background:#fff}
.brand{left:138px;top:22px;display:flex;align-items:center;gap:7px}
.brand-mark{width:22px;height:22px;border-radius:50%;background:var(--blue)}
.brand-name{font-size:16px;font-weight:300;color:var(--blue);letter-spacing:.3px;white-space:nowrap}
.search{left:564px;top:13px;width:108px;height:17px;border:1px solid #ccc;font-size:7px;color:#aaa;padding:3px 6px}
.search svg{position:absolute;right:4px;top:3px}
.socials{display:flex;gap:3px}
.socials span{width:16px;height:16px;border-radius:50%;background:#444;display:block}
.top-socials{left:677px;top:13px}
.nav{right:138px;top:42px;display:flex;font-size:9.5px;color:#666}
.nav span{padding:0 10px;border-left:1px solid #ccc}
.nav span:first-child{border:0}
.nav span:last-child{padding-right:0}

/* news */
.news{left:0;top:68px;width:868px;height:39px;background:var(--grey-bar);color:#fff;display:flex;align-items:center;justify-content:center;font-size:10px;text-transform:uppercase;gap:8px}
.news b{font-weight:700}
.btn{background:var(--blue-btn);color:#fff;font-weight:700;font-size:10px;text-transform:uppercase;padding:5px 11px;border-radius:2px;display:inline-block}

/* hero */
.hero-photo{left:0;top:107px;width:868px;height:341px;background:linear-gradient(100deg,#6e6a66 0%,#bdb8b2 30%,#e9eaeb 60%,#d7dadd 100%)}
.hero-card{left:552px;top:169px;width:240px;height:166px;background:rgba(255,255,255,.93);text-align:center;padding-top:13px}
.hero-card p{font-size:19px;line-height:25px;font-weight:400;color:#222}
.hero-card em{color:var(--blue);font-weight:700;font-style:italic}
.hero-card .btn{margin-top:10px}

/* tabs */
.tabs{left:249px;top:416px;height:81px;display:flex;box-shadow:0 4px 6px rgba(0,0,0,.12)}
.tab{width:130px;height:81px;background:linear-gradient(135deg,#fff 55%,#eceef1 56%);border-right:1px solid #ddd;text-align:center;padding-top:12px}
.tab:first-child{width:131px}
.tab:nth-child(2){width:115px}
.tab:last-child{width:124px;border:0}
.tab small{display:block;font-size:9px;letter-spacing:1.5px;color:#555;margin-top:3px}
.tab strong{display:block;font-size:15px;font-weight:400;letter-spacing:.5px;color:#444;line-height:16px}

/* quote */
.quote-band{left:0;top:448px;width:868px;height:214px;background:linear-gradient(#fff,var(--panel));border-bottom:1px solid #e3e3e3}
.h-blue{font-size:17px;font-weight:700;color:var(--blue);text-transform:uppercase}
.q-label{font-size:11px;font-weight:600;color:#444}
.amount{left:138px;top:562px;width:100px;height:26px;border:1px solid #ccc;background:#fff;font-size:11px;padding:5px 8px;color:#555}
.slider{left:246px;top:569px;width:179px;height:8px;border:1px solid #ccc;border-radius:4px;background:#fff}
.knob{left:245px;top:567px;width:13px;height:13px;border-radius:50%;background:var(--blue-light)}
.radios{left:138px;top:620px;width:290px;display:flex;justify-content:space-between}
.radio{text-align:center;font-size:10px;color:#666}
.radio i{display:block;width:11px;height:11px;border:1px solid #ccc;border-radius:50%;margin:0 auto 5px;background:#fff;position:relative}
.radio.on i::after{content:"";position:absolute;left:2px;top:2px;width:5px;height:5px;border-radius:50%;background:var(--blue)}
.divider{left:448px;top:542px;width:1px;height:108px;background:#ddd}
.row{left:470px;width:260px;display:flex;align-items:baseline;font-size:11px;font-weight:600;color:#444}
.row .dots{flex:1;border-bottom:1px solid #ccc;margin:0 6px}
.row.small{font-size:8.5px}
.note{left:470px;top:629px;width:262px;font-size:8.5px;color:#777;line-height:12px}
.note em{color:var(--blue);font-weight:700}

/* welcome */
.welcome-title{left:0;top:680px;width:868px;text-align:center;font-size:17px;font-weight:300;color:#555}
.welcome-text{left:138px;top:707px;width:592px;font-size:9px;line-height:14px;color:#555}
.welcome-text p+p{margin-top:6px}

/* how it works */
.how{left:0;top:773px;width:868px;height:246px;background:radial-gradient(ellipse at 50% 80%,var(--blue-light) 0%,var(--blue) 55%,var(--blue-deep) 100%);color:#fff}
.how-title{left:0;top:17px;width:868px;text-align:center;font-size:17px;font-weight:400}
.how-lead{left:200px;top:55px;width:468px;text-align:center;font-size:8.5px;line-height:13px}
.step{top:100px;width:172px;height:122px;border:1px solid rgba(255,255,255,.45);background:rgba(255,255,255,.05);padding:6px 11px}
.step-head{display:flex;gap:5px;align-items:flex-start}
.step-head .step-num{font-size:27px;font-weight:300;line-height:28px;padding-top:0}
.step-head .step-title{font-size:9px;line-height:13px;padding-top:3px}
.step p{font-size:8.5px;line-height:13px;margin-top:9px}
.arrow{top:153px}

/* social bar */
.social-bar{left:0;top:1019px;width:868px;height:34px;background:var(--grey-bar)}
.social-bar .socials{position:absolute;left:138px;top:9px}
.social-bar .socials span{background:#fff}
.chat{right:138px;top:9px;color:#fff;font-weight:700;font-size:10px;display:flex;align-items:center;gap:5px}

/* footer */
.f-col{top:1068px}
.f-col h4{font-size:10px;font-weight:700;color:#444;text-transform:uppercase;margin-bottom:10px}
.f-col li{list-style:none;font-size:8.5px;color:#666;margin-bottom:6px;display:flex;gap:4px}
.map{left:559px;top:1096px;width:172px;height:54px;background:linear-gradient(135deg,#c9c5bc,#a9aba3);color:#fff;font-size:8.5px;font-weight:700}
.map span{position:absolute;left:0;width:100%;text-align:center;top:34px}
.map svg{position:absolute;left:80px;top:9px}
.foot-line{left:138px;top:1169px;width:592px;height:1px;background:#ddd}
.copy{left:0;top:1180px;width:868px;text-align:center;font-size:8px;color:#666}
</style>
</head>
<body>

<header class="abs header">
  <div class="abs brand"><span class="brand-mark"></span><span class="brand-name">Meridale Capital Partners Ltd</span></div>
  <div class="abs search">SEARCH HERE...
    <svg width="10" height="10" viewBox="0 0 10 10"><circle cx="4" cy="4" r="3" fill="none" stroke="#555" stroke-width="1.4"/><line x1="6.2" y1="6.2" x2="9.3" y2="9.3" stroke="#555" stroke-width="1.6"/></svg>
  </div>
  <div class="abs socials top-socials"><span></span><span></span><span></span></div>
  <nav class="abs nav"><span>HOME</span><span>WHY MERIDALE?</span><span>SOLUTIONS</span><span>CONTACT US</span></nav>
</header>

<div class="abs news"><span><b>News :</b> Lorem ipsum dolor sit amet, consectetur adipiscing elit. In luctus dui ante.</span><span class="btn">Read More</span></div>

<div class="abs hero-photo" role="img" aria-label="Photograph of a person working at a laptop with a calculator and phone on a desk"></div>
<div class="abs hero-card">
  <p>We provide "<em>Sales Aid<br>Finance</em>" through<br>ALTERNATIVE financial<br>and <em>Contract Solutions</em>.</p>
  <span class="btn">Learn More</span>
</div>

<section class="abs quote-band"></section>

<div class="abs tabs">
  <div class="tab">
    <svg width="30" height="28" viewBox="0 0 30 28" fill="var(--blue)" stroke="var(--blue)" stroke-width="1.5"><line x1="15" y1="14" x2="5" y2="4"/><line x1="15" y1="14" x2="25" y2="4"/><line x1="15" y1="14" x2="5" y2="24"/><line x1="15" y1="14" x2="25" y2="24"/><line x1="15" y1="14" x2="15" y2="2"/><circle cx="15" cy="14" r="4.5"/><circle cx="5" cy="4" r="2.5"/><circle cx="25" cy="4" r="2.5"/><circle cx="5" cy="24" r="2.5"/><circle cx="25" cy="24" r="2.5"/><circle cx="15" cy="2" r="1.8"/></svg>
    <small>OUR AREA OF</small><strong>EXPERTIES</strong>
  </div>
  <div class="tab">
    <svg width="30" height="28" viewBox="0 0 30 28" fill="var(--blue)"><rect x="3" y="18" width="4" height="10"/><rect x="9" y="14" width="4" height="14"/><rect x="15" y="16" width="4" height="12"/><rect x="21" y="10" width="4" height="18"/><polyline points="3,14 11,8 17,12 27,3" fill="none" stroke="var(--blue)" stroke-width="2"/></svg>
    <small>WHAT WE</small><strong>FINANCE</strong>
  </div>
  <div class="tab">
    <svg width="30" height="28" viewBox="0 0 30 28" fill="none" stroke="var(--blue)" stroke-width="2"><rect x="3" y="2" width="5" height="5"/><rect x="12" y="2" width="5" height="5"/><rect x="21" y="2" width="5" height="5"/><rect x="3" y="11" width="5" height="5"/><rect x="12" y="11" width="5" height="5"/><rect x="21" y="11" width="5" height="5"/><rect x="3" y="20" width="5" height="5"/><rect x="12" y="20" width="5" height="5"/><rect x="21" y="20" width="5" height="5"/></svg>
    <small>WHY WE ARE</small><strong>EXPERTIES</strong>
  </div>
</div>

<h2 class="abs h-blue" style="left:138px;top:514px">Get an Instant Quote</h2>
<div class="abs q-label" style="left:138px;top:540px">How much do you want to borrow?</div>
<div class="abs amount">£5,000
  <svg style="position:absolute;right:5px;top:3px" width="10" height="18" viewBox="0 0 10 18" fill="none" stroke="var(--blue)" stroke-width="2"><polyline points="1,7 5,3 9,7"/><polyline points="1,11 5,15 9,11"/></svg>
</div>
<div class="abs slider"></div>
<div class="abs knob"></div>
<div class="abs q-label" style="left:138px;top:600px">How long do you want it for?</div>
<div class="abs radios">
  <div class="radio on"><i></i>6 months</div>
  <div class="radio"><i></i>1 year</div>
  <div class="radio"><i></i>2 year</div>
  <div class="radio"><i></i>3 year</div>
  <div class="radio"><i></i>4 year</div>
  <div class="radio"><i></i>5 year</div>
</div>
<div class="abs divider"></div>

<h2 class="abs h-blue" style="left:470px;top:514px">Your Quick Quote</h2>
<div class="abs row" style="top:541px"><span>Monthly repayment</span><span class="dots"></span><span>£5,000</span></div>
<div class="abs row" style="top:559px"><span>Total payable</span><span class="dots"></span><span>£10,329</span></div>
<div class="abs row small" style="top:578px"><span>Above includes Lendstone fees of</span><span class="dots"></span><span>£270</span></div>
<span class="abs btn" style="left:646px;top:598px">Apply Now</span>
<p class="abs note">Quick quote is indicative and intended as a guide only. Based on average rate of A+ risk band. <em>Learn more about costs</em></p>

<h2 class="abs welcome-title">Welcome to MCP (Meridale Capital Partners Ltd)</h2>
<div class="abs welcome-text">
  <p>We provide "Sales Aid Finance" through ALTERNATIVE financial and contract solutions. Specialising in the Print and Technology markets, we offer Value Added Resellers (VARs) a range of innovative, cost effective, value added contract and finance options to enhance their sales.</p>
  <p>Our solutions are fully financed and we are totally independent from any VAR, technology provider or traditional finance house.</p>
</div>

<section class="abs how">
  <h2 class="abs how-title">How does LedgerBridge work?</h2>
  <p class="abs how-lead">Integer dictum molestie sagittis. Pellentesque vitae nibh at mi placerat sagittis non et lorem. Sed congue nisi non pharetra convallis. Aenean aliquam non augue id bibendum.</p>
  <div class="abs step" style="left:138px">
    <div class="step-head"><span class="step-num">01.</span><span class="step-title">Register online in 15 minutes at no cost</span></div>
    <p>Apply to become a Seller on LedgerBridge quickly and simply, with no cost or obligation. Once approved you're ready to raise funding against your invoices.</p>
  </div>
  <svg class="abs arrow" style="left:326px" width="10" height="18" viewBox="0 0 10 18" fill="none" stroke="rgba(255,255,255,.5)" stroke-width="1.5"><polyline points="1,1 9,9 1,17"/></svg>
  <div class="abs step" style="left:349px">
    <div class="step-head"><span class="step-num">02.</span><span class="step-title">Submit the invoices you wish to fund</span></div>
    <p>Choose the invoices you want to raise funding against. Following verification, these are then put up for sale to the LedgerBridge investors.</p>
  </div>
  <svg class="abs arrow" style="left:536px" width="10" height="18" viewBox="0 0 10 18" fill="none" stroke="rgba(255,255,255,.5)" stroke-width="1.5"><polyline points="1,1 9,9 1,17"/></svg>
  <div class="abs step" style="left:558px">
    <div class="step-head"><span class="step-num">03.</span><span class="step-title">Invoices trade instantly and funds advanced in 24 hours</span></div>
    <p>Multiple investors buy your invoices and advance you the funds instantly. When your customer pays you, LedgerBridge returns the advance plus fees to investors.</p>
  </div>
</section>

<div class="abs social-bar">
  <div class="socials"><span></span><span></span><span></span></div>
  <div class="abs chat">
    <svg width="16" height="14" viewBox="0 0 16 14"><ellipse cx="8" cy="6" rx="8" ry="6" fill="#fff"/><polygon points="3,10 2,14 7,11" fill="#fff"/></svg>Live Chat
  </div>
</div>

<div class="abs f-col" style="left:138px"><h4>// Important Links</h4><ul><li>Home</li><li>About Us</li><li>Privacy Policy</li><li>Terms &amp; Conditions</li></ul></div>
<div class="abs f-col" style="left:273px"><h4>// Solutions</h4><ul><li>Managed Services</li><li>Public Sector</li><li>Education</li></ul></div>
<div class="abs f-col" style="left:396px"><h4>// Contact Details</h4><ul>
  <li><svg width="6" height="9" viewBox="0 0 6 9"><path d="M3 9 L0.5 4 A3 3 0 1 1 5.5 4 Z" fill="#555"/></svg><span>25, Lorem Ipsum, Dolor Sit<br>London, Heathrow, UK</span></li>
  <li><svg width="7" height="8" viewBox="0 0 7 8"><path d="M1 0 L3 2 L2 3.5 Q3 5.5 4 6 L5 5 L7 7 L6 8 Q1 7 0 1 Z" fill="#555"/></svg>0800 555 0142</li>
  <li><svg width="8" height="7" viewBox="0 0 8 7"><rect y="1" width="8" height="5" fill="#555"/><polyline points="0,1 4,4 8,1" fill="none" stroke="#fff" stroke-width=".8"/></svg>info@meridalecapital.co.uk</li>
</ul></div>
<div class="abs f-col" style="left:559px"><h4>// Location Map</h4></div>
<div class="abs map" role="img" aria-label="Street map of the office location">
  <svg width="12" height="17" viewBox="0 0 12 17"><path d="M6 17 L1 8 A6 6 0 1 1 11 8 Z" fill="#fff"/><circle cx="6" cy="6" r="2" fill="#aaa"/></svg>
  <span>View Location Map</span>
</div>
<div class="abs foot-line"></div>
<p class="abs copy">Copyright © 2014 meridalecapital.co.uk. All Rights Reserved</p>

</body>
</html>
```